Business Card Design

Tumble Bay is a Laundromat Store
we provide wash and Fold service to Customers who are busy with their life and can not come to the store and do laundry
we have customers who drop their laundry at the store
but now i want to provide service to customers who are not able to come to the store to drop. i will go to their address and pickup the laundry and get it washed folded and delivered
Updates
Can you use the colour in you design which i uploaded and also fusha fluorescent green bright pink
Target Market(s)
all works of life who don't have time to do laundry
Industry/Entity Type
Store
Contact Information for Business Card
TumbleBay Laundromat
482 Orchard Lane
Lynn MA 01957
Look and feel
Each slider illustrates characteristics of the customer's brand and the style your logo design should communicate.

```html
<!DOCTYPE html>
<html lang="en">
<head>
<meta charset="utf-8">
<title>Tumble Bay Laundromat – Pickup Card</title>
<link rel="stylesheet" href="https://fonts.googleapis.com/css2?family=Roboto+Slab:wght@300;400;700&family=Roboto:wght@300;400;700&display=swap">
<style>
  :root {
    --backdrop: #ecebe6;
    --lime: #a6ee1c;
    --lime-light: #c9f54a;
    --lime-deep: #8fe010;
    --magenta: #f01fc8;
    --violet: #7a22f0;
    --violet-deep: #5a12e0;
    --violet-light: #9a3cf5;
    --ink: #111111;
    --white: #ffffff;
    --accent-text: #c6f23a;
  }
  * { margin: 0; padding: 0; box-sizing: border-box; }
  html, body { width: 1200px; height: 1000px; overflow: hidden; }
  body { background: var(--backdrop); position: relative; font-family: "Roboto", sans-serif; }

  .card {
    position: absolute; left: 345px; top: 55px; width: 510px; height: 885px;
    overflow: hidden; box-shadow: 0 6px 18px rgba(0,0,0,.18);
  }
  .card__upper {
    position: absolute; inset: 0 0 278px 0;
    background: radial-gradient(ellipse at 70% 35%, var(--lime-light), var(--lime) 55%, var(--lime-deep));
  }
  .clothesline-art {
    position: absolute; left: 250px; top: 0; width: 260px; height: 420px;
    background: linear-gradient(180deg, rgba(255,255,255,.14), rgba(255,255,255,0));
  }
  .brand-badge {
    position: absolute; left: 17px; top: 0; width: 250px; height: 250px;
    border-radius: 50%; background: var(--white);
    display: flex; align-items: center; justify-content: center;
    box-shadow: 0 3px 8px rgba(0,0,0,.2);
  }
  .brand-badge__name {
    font-family: "Roboto Slab", serif; font-weight: 700; font-size: 38px;
    color: var(--violet); text-align: center; line-height: 1.05;
  }
  .headline { position: absolute; left: 0; right: 0; text-align: center; font-family: "Roboto Slab", serif; line-height: 1; }
  .headline--no-time { top: 292px; font-size: 52px; font-weight: 700; color: var(--ink); letter-spacing: 3px; }
  .headline--washing { top: 348px; font-size: 50px; font-weight: 300; color: var(--ink); letter-spacing: 1px; }
  .headline--pickup { top: 410px; font-size: 50px; font-weight: 300; color: var(--magenta); white-space: nowrap; }
  .headline--from { top: 466px; font-size: 52px; font-weight: 300; color: var(--magenta); letter-spacing: 4px; }
  .headline strong { font-weight: 700; }
  .service-copy {
    position: absolute; left: 0; right: 0; top: 520px; text-align: center;
    font-family: "Roboto Slab", serif; font-size: 27px; line-height: 40px; color: var(--ink);
  }
  .card__lower {
    position: absolute; left: 0; right: 0; bottom: 0; height: 278px;
    background: radial-gradient(ellipse at 35% 40%, var(--violet-light), var(--violet) 50%, var(--violet-deep));
    color: var(--white); text-align: center;
  }
  .call-line { position: absolute; left: 0; right: 0; top: 28px; font-family: "Roboto Slab", serif; font-size: 27px; }
  .call-line strong { font-weight: 700; }
  .phone {
    position: absolute; left: 0; right: 0; top: 72px;
    font-family: "Roboto Slab", serif; font-weight: 700; font-size: 62px; letter-spacing: 3px;
  }
  .divider { position: absolute; left: 0; right: 0; top: 154px; border-top: 2px dotted rgba(255,255,255,.6); }
  .business-name {
    position: absolute; left: 0; right: 0; top: 184px;
    font-weight: 300; font-size: 30px; letter-spacing: 6px; color: var(--accent-text);
  }
  .address { position: absolute; left: 0; right: 0; top: 228px; font-weight: 300; font-size: 26px; color: var(--accent-text); }
</style>
</head>
<body>
  <article class="card">
    <section class="card__upper">
      <div class="clothesline-art" role="img" aria-label="Faint line drawing of clothes hanging on a clothesline"></div>
      <div class="brand-badge"><span class="brand-badge__name">Tumble<br>Bay</span></div>
      <h1 class="headline headline--no-time">NO TIME</h1>
      <p class="headline headline--washing">FOR WASHING?</p>
      <p class="headline headline--pickup">WE NOW <strong>PICK UP</strong></p>
      <p class="headline headline--from">FROM <strong>YOU!</strong></p>
      <p class="service-copy">We will pick up, wash, fold and<br>return your clean laundry to <strong>you</strong>.</p>
    </section>
    <section class="card__lower">
      <p class="call-line"><strong>Call us now</strong> to lighten your load!</p>
      <p class="phone">781-555-0148</p>
      <div class="divider"></div>
      <p class="business-name">TUMBLEBAY LAUNDROMAT</p>
      <p class="address">482 Orchard Lane • Lynn • MA 01957</p>
    </section>
  </article>
</body>
</html>
```